Aussie Electrician needs Business Card,

Velkor Electrical Services requires a,business card design.. Company colours are black, flouo orange and silver. Refer to attached photos of company shirt.. I was thinking of basing the business card around the company shirt as company vehicle will be black with similar graphics. The business card will need to include my mobile phone number which is 0400 518 067, my business address which is P.O. Box 863, Narrabeen, N.S.W., 2101, my email which is greg@velkorelectrical.com.au as well as my contractor licence number which is 5143K

Industry/Entity Type

Business

Contact Information for Business Card

mobile: 0400 518 067, email: greg@velkorelectrical.com.au,address :P.O. Box 863 KELLMORE NSW 2187, Contractor Lic No 5143K, Greg Halloway

Requirements
Must have
• Refer to photos of shirt. Gloss black background

```html
<!DOCTYPE html>
<html lang="en">
<head>
<meta charset="utf-8">
<title>Velkor Electrical Services – Business Card</title>
<link rel="stylesheet" href="https://fonts.googleapis.com/css2?family=Big+Shoulders+Stencil+Text:wght@500;600&display=swap">
<style>
  :root {
    --page-bg: #e4e4e2;
    --card-black: #232323;
    --fluoro-orange: #e0861e;
    --silver-white: #f2f2f2;
    --card-width: 1000px;
    --card-height: 611px;
    --band-width: 140px;
  }
  * { margin: 0; padding: 0; box-sizing: border-box; }
  html, body {
    width: 1200px;
    height: 953px;
    overflow: hidden;
    background: var(--page-bg);
  }
  body {
    display: flex;
    align-items: center;
    justify-content: center;
    font-family: "Big Shoulders Stencil Text", "Arial Narrow", sans-serif;
  }
  .business-card {
    position: relative;
    width: var(--card-width);
    height: var(--card-height);
    background: var(--card-black);
    overflow: hidden;
    box-shadow: 0 10px 30px rgba(0,0,0,0.18);
  }
  .licence-band {
    position: absolute;
    left: 0; top: 0; bottom: 0;
    width: var(--band-width);
    background: var(--fluoro-orange);
  }
  .bolt {
    position: absolute;
    left: 50%;
    width: 74px;
    height: 34px;
    transform: translateX(-50%);
  }
  .bolt--top { top: 30px; }
  .bolt--bottom { bottom: 30px; }
  .licence-number {
    position: absolute;
    left: 50%;
    top: 50%;
    transform: translate(-50%, -50%) rotate(-90deg);
    white-space: nowrap;
    color: var(--silver-white);
    font-size: 40px;
    font-weight: 600;
    letter-spacing: 2px;
    line-height: 1;
    text-transform: uppercase;
  }
  .contact-list {
    position: absolute;
    left: 225px;
    top: 355px;
    list-style: none;
    color: var(--silver-white);
    font-weight: 500;
    text-transform: uppercase;
  }
  .contact-item {
    display: flex;
    align-items: center;
    height: 62px;
    letter-spacing: 1.5px;
    white-space: nowrap;
  }
  .contact-item--phone { font-size: 32px; }
  .contact-item--email { font-size: 27px; }
  .contact-item--address { font-size: 32px; }
  .contact-icon {
    width: 24px;
    height: 24px;
    margin-right: 14px;
    flex: none;
  }
</style>
</head>
<body>
  <article class="business-card" aria-label="Velkor Electrical Services business card">
    <aside class="licence-band">
      <svg class="bolt bolt--top" viewBox="0 0 74 34" aria-hidden="true">
        <polygon points="0,10 40,4 36,14 74,8 32,32 38,20 2,24" fill="var(--silver-white)"/>
      </svg>
      <p class="licence-number">Contractor Lic No 5143K</p>
      <svg class="bolt bolt--bottom" viewBox="0 0 74 34" aria-hidden="true">
        <polygon points="0,10 40,4 36,14 74,8 32,32 38,20 2,24" fill="var(--silver-white)"/>
      </svg>
    </aside>

    <ul class="contact-list">
      <li class="contact-item contact-item--phone">
        <svg class="contact-icon" viewBox="0 0 24 24" aria-hidden="true">
          <rect x="6" y="2" width="12" height="20" rx="2" fill="none" stroke="var(--fluoro-orange)" stroke-width="2"/>
        </svg>
        0400 518 067
      </li>
      <li class="contact-item contact-item--email">
        <svg class="contact-icon" viewBox="0 0 24 24" aria-hidden="true">
          <rect x="2" y="5" width="20" height="14" fill="none" stroke="var(--fluoro-orange)" stroke-width="2"/>
          <polyline points="2,5 12,13 22,5" fill="none" stroke="var(--fluoro-orange)" stroke-width="2"/>
        </svg>
        greg@velkorelectrical.com.au
      </li>
      <li class="contact-item contact-item--address">
        <svg class="contact-icon" viewBox="0 0 24 24" aria-hidden="true">
          <path d="M12 22 C6 14 5 12 5 9 A7 7 0 0 1 19 9 C19 12 18 14 12 22 Z" fill="none" stroke="var(--fluoro-orange)" stroke-width="2"/>
          <circle cx="12" cy="9" r="2.5" fill="var(--fluoro-orange)"/>
        </svg>
        P.O. Box 863 Kellmore NSW 2187, Greg Halloway
      </li>
    </ul>
  </article>
</body>
</html>
```